Trifold flyer for our dental clinic (the Bright Harbor Clinic)

The goal of this project is to design a trifold flyer for our dental clinic (the Bright Harbor Clinic). The winning design is expected to be creative, artistic and coherent with our logo.
Updates

Designs look the same

Target Market(s)

Young generation with dental need.

Industry/Entity Type

Dental Clinic

Font styles to use
Sans Serif

Colors
0355a3
85acd3
85cae6
0592cd
00a990
86cfc6
cedeed
cee9f5
cfeae6

Requirements
Must have
• See the attached sketch for content arrangement.

```html
<!DOCTYPE html>
<html lang="en">
<head>
<meta charset="utf-8">
<title>Bright Harbor Clinic — Trifold</title>
<link rel="stylesheet" href="https://fonts.googleapis.com/css2?family=Montserrat:wght@400;500;600;700;800&display=swap">
<style>
  :root{
    --navy:#0355a3;
    --blue:#2a93cc;
    --sky:#85cae6;
    --mist:#cee9f5;
    --red:#c4161c;
    --ink:#1d1d1f;
    --paper:#ffffff;
    --stage:#e6e7e9;
  }
  *{margin:0;padding:0;box-sizing:border-box}
  html,body{width:1200px;height:957px;overflow:hidden;background:var(--stage);font-family:"Montserrat",sans-serif}
  .brochure{position:absolute;left:20px;top:61px;width:1020px;height:733px;transform:scale(1.1373);transform-origin:0 0;background:var(--paper);overflow:hidden}
  .panel-shade{position:absolute;top:0;height:733px;width:343px}
  .panel-shade.left{left:0;background:linear-gradient(90deg,#fff 60%,#ececec)}
  .panel-shade.middle{left:343px;background:linear-gradient(90deg,#fff 60%,#efefef)}
  .art{position:absolute;left:0;top:0}
  .heading{position:absolute;font-weight:700;font-size:24px;color:var(--red)}
  .heading span{font-weight:500;color:var(--ink)}
  .heading::after{content:"";position:absolute;left:0;bottom:-3px;height:2px;background:var(--red)}
  .meet{left:27px;top:226px}
  .meet::after{width:84px}
  .reviews{left:374px;top:250px}
  .reviews::after{width:110px}
  .entry{position:absolute;width:260px;font-size:12.2px;line-height:14.5px;color:var(--ink)}
  .entry h3{font-size:13px;font-weight:600;color:var(--navy)}
  .quote{position:absolute;font-size:78px;font-weight:800;color:var(--blue);line-height:1;height:40px;overflow:hidden;letter-spacing:-4px}
  .review{position:absolute;width:270px;font-size:11.2px;line-height:13px;color:var(--ink)}
  .review h3{font-size:13px;font-weight:600;color:var(--navy)}
  .review.right{text-align:right}
  .brand{position:absolute;left:760px;top:160px;width:272px;text-align:center;color:#fff;font-weight:600;font-size:14px;letter-spacing:.5px}
  .brand-mark{display:block;width:26px;height:26px;border:3px solid #fff;border-radius:50%;margin:0 auto 12px}
  .call{position:absolute;left:686px;top:607px;width:334px;height:50px;background:rgba(133,202,230,.55);text-align:center;color:var(--red);font-weight:800}
  .call .lead{font-size:19px;line-height:20px;margin-top:3px}
  .call .phone{font-size:21px;letter-spacing:5px;line-height:22px}
  .offers{position:absolute;left:686px;top:657px;width:334px;height:76px;background:var(--blue);color:#fff;display:flex;align-items:center}
  .offers .label{width:105px;padding-left:16px;font-weight:600;font-size:16px;line-height:20px;border-right:1px solid #fff;height:50px;display:flex;align-items:center}
  .offers ul{list-style:none;padding-left:12px;font-size:15px;line-height:18px}
</style>
</head>
<body>
<div class="brochure">
  <div class="panel-shade left"></div>
  <div class="panel-shade middle"></div>

  <svg class="art" width="1020" height="733" viewBox="0 0 1020 733">
    <!-- band strokes -->
    <polyline points="0,110 200,222 445,0" fill="none" stroke="var(--sky)" stroke-width="12" stroke-linejoin="round"/>
    <polyline points="343,132 618,328 760,190" fill="none" stroke="var(--sky)" stroke-width="12" stroke-linejoin="round"/>
    <polyline points="686,262 778,180 1000,368 1020,368" fill="none" stroke="var(--sky)" stroke-width="10" stroke-linejoin="round"/>
    <polyline points="735,150 865,0" fill="none" stroke="var(--sky)" stroke-width="10"/>
    <!-- photo areas -->
    <path role="img" aria-label="Photo: two doctors meeting at a desk with a laptop" d="M0,0 H440 L228,186 Q200,210 172,190 L0,95 Z" fill="#b9c3cc"/>
    <path role="img" aria-label="Photo: smiling young woman in warm sunset light" d="M452,0 H850 L768,140 L648,300 Q620,322 592,304 L345,122 Z" fill="#b9845f"/>
    <path role="img" aria-label="Photo: dentist with loupes treating a patient" d="M686,258 L778,176 L990,358 H1020 V607 H686 Z" fill="#5f6f85"/>
    <!-- brand field -->
    <path d="M862,0 H1020 V345 H985 Q970,345 955,335 L758,180 Q745,160 758,140 Z" fill="var(--blue)"/>
  </svg>

  <h2 class="heading meet">Meet <span>Us</span></h2>
  <div class="entry" style="left:27px;top:302px"><h3>Dr. Marlen Ostrow</h3>Lorem ipsum dolor sit amet, consec-tetuer adipiscing elit, sed diam nonum-my nibh euismod tincidunt ut laoreet dolore magna</div>
  <div class="entry" style="left:27px;top:413px"><h3>Dr. Marlen Ostrow</h3>Lorem ipsum dolor sit amet, consec-tetuer adipiscing elit, sed diam nonum-my nibh euismod tincidunt ut laoreet dolore magna</div>
  <div class="entry" style="left:27px;top:518px"><h3>Dr. Marlen Ostrow</h3>Lorem ipsum dolor sit amet, consec-tetuer adipiscing elit, sed diam nonum-my nibh euismod tincidunt ut laoreet dolore magna</div>
  <div class="entry" style="left:27px;top:624px"><h3>Dr. Marlen Ostrow</h3>Lorem ipsum dolor sit amet, consec-tetuer adipiscing elit, sed diam nonum-my nibh euismod tincidunt ut laoreet dolore magna</div>

  <h2 class="heading reviews">Reviews</h2>
  <div class="quote" style="left:376px;top:320px">“</div>
  <div class="review" style="left:378px;top:373px"><h3>Marlen Ostrow</h3>Lorem ipsum dolor sit amet, consectetuer adipiscing elit, sed diam nonummy nibh euismod tincidunt ut laoreet dolore magna</div>
  <div class="quote" style="left:577px;top:458px">“</div>
  <div class="review right" style="left:369px;top:496px"><h3>Teodor Vance</h3>Lorem ipsum dolor sit amet, consectetuer adipiscing elit, sed diam nonummy nibh euismod tincidunt ut laoreet dolore magna</div>
  <div class="quote" style="left:378px;top:582px">“</div>
  <div class="review" style="left:378px;top:626px"><h3>Ilsa Marquet</h3>Lorem ipsum dolor sit amet, consectetuer adipiscing elit, sed diam nonummy nibh euismod tincidunt ut laoreet dolore magna</div>

  <div class="brand" style="left:760px;top:118px;width:272px"><span class="brand-mark"></span>BRIGHT HARBOR CLINIC</div>

  <div class="call"><div class="lead">Call us now!</div><div class="phone">55-014-2290</div></div>
  <div class="offers">
    <div class="label">SPECIAL OFFERS:</div>
    <ul><li>$69 | New Patient</li><li>$99 | Teeth Whitening</li><li>25% - 40% | on Clearline</li></ul>
  </div>
</div>
</body>
</html>
```